Beauty Clinic Treatment Menu (Lumen Nails & Beauty)

Needing a treatment menu designed for a beauty clinic in Korimako Bay, New Zealand. Like the colours grey, pink, white.
Elegant, Modern and feminine

Lumen Nails & Beauty
Karen Pell
Room3, 48 Tainui Street
Korimako Bay
0273816240
Karen.lumen@mailbox.test
lumenbeauty.co.nz

Target Market(s)

Females

Industry/Entity Type

Beauty Salon

Font styles to use
Serif

Colors

Requirements
Must have
• Chatterly and Snapgrid logo

```html
<!DOCTYPE html>
<html lang="en">
<head>
<meta charset="utf-8">
<title>Lumen Nails &amp; Beauty – Treatment Menu</title>
<link rel="stylesheet" href="https://fonts.googleapis.com/css2?family=Montserrat:wght@400;500;600;700;800&display=swap">
<style>
  :root{
    --stage:#eedff0;
    --lilac:#dcaeea;
    --lilac-deep:#c99ad9;
    --mauve:#8e7395;
    --charcoal:#5b5b5d;
    --ink:#555457;
    --blush:#f3cfe2;
    --blush-soft:#f8e7f0;
    --white:#ffffff;
    --mist:#ececee;
    --copper:#a8785c;
    --copper-light:#d7ae93;
  }
  *{margin:0;padding:0;box-sizing:border-box}
  html,body{width:1200px;height:1200px;overflow:hidden}
  body{
    background:radial-gradient(ellipse at center,#f6ecf5 0%,var(--stage) 70%);
    font-family:"Montserrat",sans-serif;
    color:var(--ink);
    position:relative;
  }
  .brochure{
    position:absolute;left:104px;top:255px;width:992px;height:690px;
    overflow:hidden;
    box-shadow:0 18px 40px rgba(160,110,170,.35);
  }
  .panel{position:absolute;top:0;height:690px}
  .panel--left{left:0;width:331px;background:linear-gradient(180deg,var(--blush-soft),#fff 80%)}
  .panel--middle{left:331px;width:330px;background:linear-gradient(90deg,var(--lilac-deep) 0%,var(--lilac) 25%,var(--lilac) 80%,var(--lilac-deep) 100%)}
  .panel--right{left:661px;width:331px;background:linear-gradient(90deg,var(--mist),var(--white) 30%,var(--white) 80%,#f2f2f3)}
  .shapes{position:absolute;inset:0;width:992px;height:690px}

  .ring{position:absolute;border-radius:50%;border:2px solid var(--copper);display:flex;flex-direction:column;align-items:center;justify-content:center;text-align:center}
  .ring--info{left:94px;top:308px;width:200px;height:200px;background:rgba(255,255,255,.35);padding:22px 14px}
  .info-text{font-size:8.6px;font-weight:600;line-height:1.52;color:var(--ink)}
  .ring--mid{left:431px;top:59px;width:130px;height:130px;border-color:var(--white)}
  .ring--right{left:738px;top:46px;width:180px;height:180px}
  .brand-name{font-weight:500;font-size:26px;letter-spacing:1px;line-height:1}
  .brand-name--mid{color:var(--white);font-size:24px}
  .brand-name--right{color:var(--copper);font-size:34px}
  .brand-tag{font-size:7.5px;margin-top:10px;color:var(--white)}
  .brand-tag--right{font-size:9.5px;color:var(--copper-light)}

  .owner-pill{position:absolute;left:702px;top:237px;width:245px;height:36px;border-radius:18px;background:var(--charcoal);color:var(--white);font-weight:800;font-size:16px;letter-spacing:4px;display:flex;align-items:center;justify-content:center;box-shadow:3px 4px 6px rgba(0,0,0,.2)}
  .owner-pill .dot{color:var(--lilac)}

  .map{position:absolute;left:367px;top:216px;width:253px;height:116px;border-radius:6px;background:linear-gradient(90deg,#e4e2df 0%,#ebe9e6 70%,#a6d0f7 82%);box-shadow:2px 3px 6px rgba(0,0,0,.12)}
  .contact{position:absolute;left:331px;width:330px;text-align:center;color:var(--ink)}
  .visit{top:358px;font-weight:800;font-size:14px}
  .url-pill{position:absolute;left:371px;top:398px;width:245px;height:35px;border-radius:18px;background:var(--white);font-weight:800;font-size:13.5px;display:flex;align-items:center;justify-content:center;box-shadow:3px 3px 5px rgba(0,0,0,.15)}
  .address{top:456px;font-weight:800;font-size:14px;line-height:20.5px}
  .phone{top:532px;font-size:14.5px;font-weight:500}
  .phone strong{font-weight:800}
  .email{top:564px;font-weight:800;font-size:14.5px}
  .social{top:603px;display:flex;justify-content:center;gap:16px;font-size:10px;font-weight:700}
  .social-item{display:flex;align-items:center;gap:5px}
  .social-dot{width:24px;height:24px;border-radius:50%;background:var(--charcoal)}
</style>
</head>
<body>
<main class="brochure">
  <section class="panel panel--left"></section>
  <section class="panel panel--middle"></section>
  <section class="panel panel--right"></section>

  <svg class="shapes" viewBox="0 0 992 690">
    <defs>
      <linearGradient id="blushPhoto" x1="0" y1="0" x2="1" y2="1">
        <stop offset="0" stop-color="#f7d8e8"/><stop offset="1" stop-color="#efc3dc"/>
      </linearGradient>
      <linearGradient id="spaPhoto" x1="0" y1="0" x2="0" y2="1">
        <stop offset="0" stop-color="#f8e4ef" stop-opacity="0"/><stop offset=".45" stop-color="#f6dccd"/><stop offset=".85" stop-color="#e8b79a"/><stop offset="1" stop-color="#d8a36e"/>
      </linearGradient>
      <linearGradient id="handPhoto" x1="0" y1="0" x2="1" y2="1">
        <stop offset="0" stop-color="#ffffff"/><stop offset=".45" stop-color="#f0cfc0"/><stop offset=".8" stop-color="#e6b8a6"/><stop offset="1" stop-color="#f5f5f5"/>
      </linearGradient>
    </defs>

    <g class="left-photo-lower" role="img" aria-label="Photo of hands resting on smooth legs with pink flowers and black spa stones">
      <rect x="0" y="380" width="331" height="310" fill="url(#spaPhoto)"/>
    </g>
    <path class="band band--grey" d="M0 0 H331 V182 C300 300 120 290 0 372 Z" fill="var(--charcoal)"/>
    <path class="band band--mauve" d="M0 0 H331 V166 C300 282 120 276 0 354 Z" fill="var(--mauve)"/>
    <g role="img" aria-label="Photo of glossy pink lips showing through torn pink paper">
      <path class="left-photo-upper" d="M0 0 H331 V150 C300 262 120 262 0 336 Z" fill="url(#blushPhoto)"/>
    </g>

    <path class="band band--grey" d="M992 258 C950 350 720 370 645 455 C600 510 595 620 630 690 H992 Z" fill="var(--charcoal)"/>
    <path class="band band--mauve" d="M992 290 C950 380 735 392 660 470 C617 520 611 625 640 690 H992 Z" fill="var(--mauve)"/>
    <path d="M992 306 C950 394 745 406 672 480 C630 526 625 628 652 690 H992 Z" fill="var(--white)"/>
    <g role="img" aria-label="Photo of a hand with long almond nails in glossy royal blue gel polish">
      <path d="M700 460 C760 440 880 430 980 450 L985 690 H715 C690 600 690 520 700 460 Z" fill="url(#handPhoto)" opacity=".85"/>
    </g>
  </svg>

  <div class="ring ring--info">
    <p class="info-text">The Petalcoat Labs™ gel polishes are rich, highly pigmented, chip-resistant and offer extreme long lasting shine. The good news doesn't end there because Petalcoat is VEGAN, CRUELTY FREE and 10-FREE (our products don't contain formaldehyde, Dibutyl phthalate, toluene, formaldehyde resin or camphor).</p>
  </div>

  <div class="ring ring--mid">
    <span class="brand-name brand-name--mid">Lumen</span>
    <span class="brand-tag">Nails &amp; Beauty</span>
  </div>

  <div class="map" role="img" aria-label="Street map of the town centre with a pin on Tainui Street beside the harbour"></div>
  <p class="contact visit">VISIT US</p>
  <div class="url-pill">www.lumenbeauty.co.nz</div>
  <p class="contact address">Karen Pell, Room3,<br>48 Tainui Street<br>Korimako Bay</p>
  <p class="contact phone"><strong>Phone:</strong> 0273816240</p>
  <p class="contact email">Karen.lumen@mailbox.test</p>
  <div class="contact social">
    <span class="social-item"><span class="social-dot"></span>Chatterly</span>
    <span class="social-item"><span class="social-dot"></span>Snapgrid</span>
  </div>

  <div class="ring ring--right">
    <span class="brand-name brand-name--right">Lumen</span>
    <span class="brand-tag brand-tag--right">Nails &amp; Beauty</span>
  </div>
  <div class="owner-pill">BY KAREN PELL<span class="dot">.</span></div>
</main>
</body>
</html>
```